Carton Box Packaging For Motorcycle Electric Regulator - Verosta Brand

Packaging Dimensions: 7cm (H) x 6cm (W) x 2.5cm (D)
We would like to design a genuine Carton box Packaging for motorcycle electric regulator.
This is a sensitive part of the motorcycle, so we need the packaging to reflect elegant impression.
Verosta, is one of the leading companies for manufacturing Motorcycles, located in Egypt. Our company is offering high-quality products, the best in the local market, with very competitive prices.
We have a limited time to get this project done, So we Highly appreciate receiving your designs ASAP.
Target Market(s)
Motorcycle Parts Buyers
Font styles to use
Colors
Designer to choose colors to be used in the design.
Look and feel
Each slider illustrates characteristics of the customer's brand and the style your logo design should communicate.

```html
<!DOCTYPE html>
<html lang="en">
<head>
<meta charset="utf-8">
<title>Verosta Motorcycle Regulator – Carton Box</title>
<link href="https://fonts.googleapis.com/css2?family=Russo+One&family=Saira+Condensed:wght@500;600&display=swap" rel="stylesheet">
<style>
  :root{
    --backdrop:#e4e4e4;
    --black:#121212;
    --graphite:#3b3b3d;
    --silver:#d9d9d9;
    --silver-light:#f2f2f2;
    --silver-mid:#a9a9ab;
    --navy:#0b0f5c;
    --navy-deep:#05073a;
    --red:#c40f19;
    --white:#ffffff;
  }
  *{margin:0;padding:0;box-sizing:border-box}
  html,body{width:1200px;height:809px;overflow:hidden}
  body{background:var(--backdrop);position:relative;font-family:"Saira Condensed",sans-serif}

  .carton{position:absolute;left:125px;top:175px;display:flex;height:460px}
  .panel{position:relative;height:460px;overflow:hidden}
  .panel--side{width:130px;
    background:linear-gradient(180deg,var(--black) 0%,var(--graphite) 40%,var(--silver-mid) 62%,var(--silver-light) 70%,var(--silver-mid) 78%,var(--graphite) 92%,var(--black) 100%)}
  .panel--face{width:345px;
    background:linear-gradient(180deg,var(--black) 0%,var(--graphite) 38%,var(--silver-mid) 62%,var(--silver-light) 76%,var(--silver) 100%)}

  .band{position:absolute;inset:0;width:100%;height:100%}

  .side-brand{position:absolute;left:50%;top:50%;transform:translate(-50%,-50%) rotate(90deg);
    font-family:"Russo One",sans-serif;font-size:34px;letter-spacing:3px;color:var(--silver);white-space:nowrap}

  .brand{position:absolute;display:flex;align-items:center;gap:10px;
    font-family:"Russo One",sans-serif;color:var(--silver);letter-spacing:3px}
  .brand__dot{border:3px solid var(--silver);border-radius:50%}
  .brand--front{left:30px;top:36px;font-size:42px}
  .brand--front .brand__dot{width:44px;height:44px}
  .brand--back{right:22px;top:50px;font-size:28px}
  .brand--back .brand__dot{width:32px;height:32px}

  .product-photo{position:absolute;left:28px;top:108px;width:290px;height:262px;border-radius:6px;
    background:radial-gradient(ellipse at 60% 40%,#4a4a4c 0%,#262627 45%,rgba(30,30,30,0) 75%)}

  .quality-badge{position:absolute;left:274px;top:330px;width:50px;height:96px;border-radius:5px;
    background:linear-gradient(180deg,#f4f4f4,#8d8d90);border:1px solid #555}

  .title{position:absolute;font-family:"Russo One",sans-serif;line-height:1}
  .title__kicker{display:block;color:var(--silver);font-size:15px;letter-spacing:.5px}
  .title__main{display:block;color:var(--red);font-size:36px;letter-spacing:1px;margin-top:3px}
  .title--front{left:28px;top:396px}
  .title--back{left:78px;top:194px}

  .maker{position:absolute;left:12px;bottom:12px;color:var(--white);font-size:8.5px;line-height:1.35}
  .maker__label{font-weight:600}
</style>
</head>
<body>
  <div class="carton">
    <section class="panel panel--side">
      <span class="side-brand">VEROSTA</span>
    </section>

    <section class="panel panel--face panel--front">
      <svg class="band" viewBox="0 0 345 460" preserveAspectRatio="none" aria-hidden="true">
        <path d="M0,298 C70,380 180,392 280,390 L345,388 L345,460 L0,460 Z" fill="var(--navy)"/>
        <path d="M0,298 C70,380 180,392 280,390 L345,388" fill="none" stroke="var(--silver-light)" stroke-width="4"/>
      </svg>
      <div class="brand brand--front"><span>VEROSTA</span><span class="brand__dot"></span></div>
      <div class="product-photo" role="img" aria-label="Product photo: black finned motorcycle voltage regulator with red, yellow and green wires leading to a white connector"></div>
      <div class="quality-badge" aria-hidden="true"></div>
      <h1 class="title title--front"><span class="title__kicker">MOTORCYCLE</span><span class="title__main">REGULATOR</span></h1>
    </section>

    <section class="panel panel--side">
      <span class="side-brand">VEROSTA</span>
    </section>

    <section class="panel panel--face panel--back">
      <svg class="band" viewBox="0 0 345 460" preserveAspectRatio="none" aria-hidden="true">
        <path d="M0,405 L130,402 C240,398 310,360 345,276 L345,460 L0,460 Z" fill="var(--navy)"/>
        <path d="M0,405 L130,402 C240,398 310,360 345,276" fill="none" stroke="var(--silver-light)" stroke-width="4"/>
      </svg>
      <div class="brand brand--back"><span>VEROSTA</span><span class="brand__dot"></span></div>
      <h2 class="title title--back"><span class="title__kicker">MOTORCYCLE</span><span class="title__main">REGULATOR</span></h2>
      <p class="maker"><span class="maker__label">manufactured and distributed by:</span><br>VEROSTA CO.LTD<br>EGYPT</p>
    </section>
  </div>
</body>
</html>
```